Leading In-Home Tutoring Company Needs Web Banners

We need a suite of web banners for our re-marketing campaign. We are based in Melbourne and heading into the busiest time of the year with back to school and we would like to help guide parents to working with us via quality designed banners with the right CTAs. Banner specs as follows (W x H in pixels)
Medium Rectangle: 300 x 250
Vertical rectangle: 240 x 400
Banner: 468 x 60
Leaderboard: 728 x 90
Square: 250 x 250
Mobile leaderboard: 320 x 50
Updates

Hi designers I'm new to this and didn't realise that I had to upload all files at the beginning. I have images that can be used for this project. Just need to work out how to upload them. Added Sunday, January 22, 2017

Hi awesome designers... I've updated the brief now with new files :)

Target Market(s)

Mothers who value kids education. Our customer can be found having morning coffee with friends in her lycra as she prepares to go to the gym. Middle class, inner city and suburban Mums. Most likely on Chatterloom.

Industry/Entity Type

It Company

Font styles to use
Sans Serif

Colors
0692cd
fbed22
f47f39
ec1f27

Requirements
Must have
• Wording should include.
• What we do: 1:1, In-Home Tutoring
• Value proposition: The Best Tutor For Your Child
• Call to Action - Free Assessment > Find Out More
• Adjusted layout to suit the sizes. Use of image where possible to provide immediate graphic display of what we do
Nice to have
• Keep it simple, create an emotive connection. Kids matter to parents and they will pay for services if we can create banners that show we care and can help wtih their education.
Should not have
• Anything negative or use fear marketing

```html
<!DOCTYPE html>
<html lang="en">
<head>
<meta charset="utf-8">
<title>In-Home Tutoring Web Banners</title>
<link rel="stylesheet" href="https://fonts.googleapis.com/css2?family=Poppins:wght@500;600;700&family=Open+Sans:wght@400;600&family=Roboto+Condensed:wght@300;400&display=swap">
<style>
  :root {
    --stage: #3b2419;
    --label: #ffffff;
    --maroon-top: #7a1222;
    --maroon-bottom: #3b0911;
    --yellow: #fbed22;
    --blue: #0692cd;
    --orange: #f47f39;
    --red: #ec1f27;
    --white: #ffffff;
    --ink: #2a1a12;
    --brick-top: #c05a32;
    --brick-bottom: #8e3b22;
    --board-top: #3f6b4c;
    --board-bottom: #2c5038;
    --board-frame: #e9e7e3;
    --chalk: #f3f3ee;
  }
  * { box-sizing: border-box; margin: 0; padding: 0; }
  html, body { width: 1200px; height: 1000px; overflow: hidden; }
  body { background: var(--stage); position: relative; font-family: "Open Sans", Arial, sans-serif; }

  .option-label {
    position: absolute; width: 300px; text-align: center;
    font-family: "Roboto Condensed", Arial, sans-serif; font-weight: 300;
    font-size: 30px; color: var(--label); line-height: 1;
  }
  .banner { position: absolute; overflow: hidden; box-shadow: 0 4px 14px rgba(0,0,0,.45); }
  .banner > * { position: absolute; }
  .headline { font-family: "Poppins", Arial, sans-serif; font-weight: 700; left: 0; right: 0; text-align: center; line-height: 1; }
  .tagline { left: 0; right: 0; text-align: center; color: var(--white); line-height: 1; }
  .photo { left: 0; right: 0; }
  .cta-button {
    display: flex; align-items: center; justify-content: center;
    font-size: 13px; line-height: 1; text-decoration: none;
  }
  .cta-button--yellow { background: var(--yellow); color: var(--ink); }
  .cta-button--blue { background: var(--blue); color: var(--white); font-family: "Poppins", Arial, sans-serif; font-weight: 500; }
  .cta-button--red { background: var(--red); color: var(--white); font-family: "Roboto Condensed", Arial, sans-serif; font-weight: 400; font-size: 15px; }
  .offer { font-family: "Poppins", Arial, sans-serif; font-weight: 600; color: var(--white); line-height: 1; white-space: nowrap; }
  .offer .highlight { color: var(--yellow); }

  .banner--maroon { background: linear-gradient(180deg, var(--maroon-top), var(--maroon-bottom)); }
  .classroom-photo { background: linear-gradient(135deg, #d9dde4 0%, #8aa6c8 40%, #3d5f93 70%, #1e2c4a 100%); }

  .brick-scene { inset: 0; background: linear-gradient(180deg, var(--brick-top), var(--brick-bottom)); }
  .students-photo { left: 0; right: 0; top: 150px; bottom: 0; background: linear-gradient(180deg, rgba(40,60,55,0) 0%, #2f4a44 45%, #1f2e30 100%); }

  .banner--board { background: var(--board-frame); }
  .chalkboard { left: 0; right: 14px; top: 0; height: 170px; background: linear-gradient(180deg, var(--board-top), var(--board-bottom)); }
  .board-text { font-family: "Roboto Condensed", Arial, sans-serif; font-weight: 400; line-height: 1; white-space: nowrap; }
  .board-text--light { color: var(--chalk); left: 0; right: 14px; text-align: center; }
  .board-text--dark { color: var(--ink); left: 25px; }
</style>
</head>
<body>

  <div class="option-label" style="left:98px; top:312px;">Option-01</div>
  <div class="option-label" style="left:431px; top:164px;">Option-02</div>
  <div class="option-label" style="left:768px; top:312px;">Option-03</div>
  <div class="option-label" style="left:253px; top:653px;">Option-04</div>
  <div class="option-label" style="left:630px; top:653px;">Option-05</div>

  <!-- Option 01: medium rectangle -->
  <section class="banner banner--maroon" style="left:97px; top:357px; width:300px; height:250px;">
    <h2 class="headline" style="top:9px; font-size:20px; color:var(--yellow);">1:1, In-Home Tutoring</h2>
    <p class="tagline" style="top:36px; font-size:16px;">The Best Tutor For Your Child</p>
    <div class="photo classroom-photo" role="img" aria-label="Tutor helping a schoolboy with his work at a desk in front of bookshelves" style="top:61px; height:148px;"></div>
    <p class="offer" style="left:21px; top:221px; font-size:15px;"><span class="highlight">Free</span> Assessment</p>
    <a class="cta-button cta-button--yellow" style="left:162px; top:219px; width:113px; height:20px;">Find Out More</a>
  </section>

  <!-- Option 02: vertical rectangle -->
  <section class="banner banner--maroon" style="left:461px; top:207px; width:240px; height:400px;">
    <h2 class="headline" style="top:18px; font-size:26px; color:var(--white);">1:1, IN-HOME</h2>
    <h2 class="headline" style="top:47px; font-size:30px; color:var(--yellow);">TUTORING</h2>
    <p class="tagline" style="top:85px; font-size:14.5px;">The Best Tutor For Your Child</p>
    <div class="photo classroom-photo" role="img" aria-label="Tutor helping a schoolboy with his work at a desk in front of bookshelves" style="top:119px; height:181px;"></div>
    <p class="offer" style="left:0; right:0; text-align:center; top:318px; font-size:22px;"><span class="highlight">Free</span> Assessment</p>
    <a class="cta-button cta-button--blue" style="left:51px; top:354px; width:138px; height:25px;">FIND OUT MORE</a>
  </section>

  <!-- Option 03: arrows header on brick -->
  <section class="banner" style="left:781px; top:357px; width:300px; height:250px;">
    <div class="brick-scene" role="img" aria-label="Red brick wall background"></div>
    <div class="students-photo" role="img" aria-label="Group of smiling school children in uniform standing against the wall"></div>
    <svg style="left:0; top:6px;" width="300" height="54" viewBox="0 0 300 54" aria-hidden="true">
      <polygon points="300,14 168,14 168,2 145,27 168,52 168,40 300,40" fill="var(--blue)"/>
      <polygon points="0,14 145,14 145,2 168,27 145,52 145,40 0,40" fill="var(--yellow)"/>
    </svg>
    <h2 class="headline" style="left:28px; right:auto; top:22px; font-size:18px; color:var(--blue);">1:1, In-Home</h2>
    <h2 class="headline" style="left:168px; right:auto; top:22px; font-size:18px; color:var(--yellow);">Tutoring</h2>
    <p class="offer" style="left:0; right:0; text-align:center; top:65px; font-size:15.5px;">The Best Tutor For Your Child</p>
    <p class="offer" style="left:0; right:0; text-align:center; top:89px; font-size:15.5px; color:var(--yellow);">Free Assessment</p>
    <a class="cta-button cta-button--yellow" style="left:84px; top:114px; width:130px; height:20px;">Find Out More</a>
  </section>

  <!-- Option 04: brick -->
  <section class="banner" style="left:248px; top:695px; width:300px; height:250px;">
    <div class="brick-scene" role="img" aria-label="Red brick wall background"></div>
    <div class="students-photo" role="img" aria-label="Group of smiling school children in uniform standing against the wall"></div>
    <h2 class="headline" style="top:20px; font-size:20px; color:var(--yellow);">1:1, In-Home Tutoring</h2>
    <p class="tagline" style="top:48px; font-size:16px;">The Best Tutor For Your Child</p>
    <p class="offer" style="left:0; right:0; text-align:center; top:80px; font-size:16px;">Free Assessment</p>
    <a class="cta-button cta-button--yellow" style="left:93px; top:109px; width:112px; height:20px;">Find Out More</a>
  </section>

  <!-- Option 05: board -->
  <section class="banner banner--board" style="left:630px; top:695px; width:300px; height:250px;">
    <div class="chalkboard" role="img" aria-label="Green school chalkboard with a ledge and duster below"></div>
    <h2 class="board-text board-text--light" style="top:28px; font-size:38px;">1:1, IN-HOME</h2>
    <h2 class="board-text board-text--light" style="top:70px; font-size:38px;">TUTORING</h2>
    <p class="board-text board-text--light" style="top:120px; font-size:18px;">THE BEST TUTOR FOR YOUR CHILD</p>
    <p class="board-text board-text--dark" style="top:180px; font-size:22px;">FREE ASSESSMENT</p>
    <a class="cta-button cta-button--red" style="left:25px; top:208px; width:130px; height:24px;">FIND OUT MORE</a>
  </section>

</body>
</html>
```